Accommodation in an Executive Apartment for rent could be a Bed and breakfast,

Currently have a website and like the overall look but it needs revamping and want to add an instant booking button, which I would do later as the unit has a channel manager. Also want to be able to post blogs, etc. Need it to be viewed well on smart phones/tablets. all information related to this unit is on the current site which is www.lorvenstaysmirrabrook.com.au if you would view websites similar to staywell.example and roamtrip.example Must be able to be coded in Wordpress

The current design is done in Wordpress so would want this functionality in any new design.

Target Market(s)

Workers at Quorran precinct, Canberra. Workers at Halvern centre Deakin, Workers at Marlow Peter Tenby Hospital, Workers at Brindlewood Hospital, Public Servants Woden, Workers in Deakin ACT

Industry/Entity Type

Accommodation

Number of Pages Required

5+ page

Font styles to use
Sans Serif

Colors
ec1f27

Requirements
Must have
• Must have a classy look about it. Less clicks through the better. Not to wordy. Hard hitting points,
Nice to have
• Would like to retain the same colour theme and look
Should not have
• anything tacky

```html
<!DOCTYPE html>
<html lang="en">
<head>
<meta charset="utf-8">
<title>Lorven Executive Bed &amp; Breakfast – Booking Details</title>
<link rel="stylesheet" href="https://fonts.googleapis.com/css2?family=Arimo:wght@400;700&family=Cabin:wght@400;500&display=swap">
<style>
  :root {
    --brand-red: #d8391f;
    --brand-red-deep: #b8231a;
    --brand-red-light: #e84a2c;
    --nav-cream: #f2e8d0;
    --nav-cream-deep: #e6d8b4;
    --nav-rule: #c9b98e;
    --nav-text: #3a342a;
    --page-bg: #f9f8f6;
    --text-main: #1e1e1e;
    --text-muted: #777777;
    --field-border: #9b2c2c;
    --field-bg: #ffffff;
    --button-text: #c0241b;
    --footer-bg: #1e1e1e;
    --footer-text: #dedede;
  }
  * { box-sizing: border-box; margin: 0; padding: 0; }
  html, body {
    width: 1167px;
    height: 1200px;
    overflow: hidden;
  }
  body {
    position: relative;
    background: var(--page-bg);
    font-family: "Arimo", Arial, sans-serif;
    color: var(--text-main);
  }

  /* Header band */
  .site-header {
    position: absolute;
    left: 0; top: 0;
    width: 1167px; height: 136px;
    background: radial-gradient(ellipse at 50% 40%, var(--brand-red-light) 0%, var(--brand-red) 45%, var(--brand-red-deep) 100%);
  }
  .brand-name {
    position: absolute;
    left: 0; top: 58px;
    width: 1167px;
    text-align: center;
    font-family: "Cabin", sans-serif;
    font-weight: 500;
    font-size: 24px;
    letter-spacing: 1px;
    color: #ffffff;
  }

  /* Navigation */
  .main-nav {
    position: absolute;
    left: 0; top: 136px;
    width: 1167px; height: 57px;
    background: linear-gradient(to bottom, var(--nav-cream) 0%, var(--nav-cream-deep) 100%);
    border-bottom: 2px solid var(--nav-rule);
  }
  .nav-link {
    position: absolute;
    top: 20px;
    transform: translateX(-50%);
    font-family: "Cabin", sans-serif;
    font-size: 16px;
    letter-spacing: 1.6px;
    color: var(--nav-text);
    text-decoration: none;
  }

  /* Stay dates */
  .stay-label, .stay-value {
    position: absolute;
    font-size: 16px;
    color: #111111;
  }
  .stay-label { top: 289px; }
  .stay-value { top: 316px; }
  .stay-value strong { font-weight: 700; }

  /* Form */
  .field-label {
    position: absolute;
    font-size: 16px;
    color: #222222;
  }
  .field-input {
    position: absolute;
    background: var(--field-bg);
    border: 1px solid var(--field-border);
    border-radius: 4px;
  }
  .field-note {
    position: absolute;
    left: 628px; top: 561px;
    font-size: 13px;
    color: var(--text-muted);
  }
  .confirm-button {
    position: absolute;
    left: 666px; top: 991px;
    width: 252px; height: 50px;
    background: var(--field-bg);
    border: 1px solid var(--field-border);
    border-radius: 4px;
    font-family: "Arimo", Arial, sans-serif;
    font-weight: 700;
    font-size: 18px;
    letter-spacing: 2.5px;
    color: var(--button-text);
  }

  /* Footer */
  .site-footer {
    position: absolute;
    left: 0; top: 1157px;
    width: 1167px; height: 43px;
    background: var(--footer-bg);
  }
  .footer-text {
    position: absolute;
    top: 12px;
    font-size: 16px;
    color: var(--footer-text);
  }
</style>
</head>
<body>
  <header class="site-header" role="img" aria-label="Red header band with a subtle scale pattern behind the business name">
    <div class="brand-name">Lorven Executive Bed &amp; Breakfast</div>
  </header>

  <nav class="main-nav">
    <a class="nav-link" style="left:140px" href="#">HOME</a>
    <a class="nav-link" style="left:347px" href="#">FACILITY</a>
    <a class="nav-link" style="left:582px" href="#">NEARBY</a>
    <a class="nav-link" style="left:815px" href="#">GALLERY</a>
    <a class="nav-link" style="left:1010px" href="#">CONTACT</a>
  </nav>

  <main class="booking-form">
    <div class="stay-label" style="left:236px">Check-in:</div>
    <div class="stay-value" style="left:236px">Wednesday <strong>2 March</strong> 2016 from 14:00</div>
    <div class="stay-label" style="left:666px">Check-out:</div>
    <div class="stay-value" style="left:666px">Thursday 3 March 2016 until 12:00</div>

    <label class="field-label" style="left:237px; top:397px">Title</label>
    <div class="field-input" style="left:236px; top:424px; width:69px; height:51px"></div>

    <label class="field-label" style="left:363px; top:397px">First Name</label>
    <div class="field-input" style="left:363px; top:424px; width:251px; height:51px"></div>

    <label class="field-label" style="left:666px; top:397px">Last Name</label>
    <div class="field-input" style="left:666px; top:424px; width:252px; height:51px"></div>

    <label class="field-label" style="left:236px; top:514px">Email Address</label>
    <div class="field-input" style="left:236px; top:539px; width:380px; height:54px"></div>
    <div class="field-note">* We'll send a confirmation email to this address.</div>

    <label class="field-label" style="left:237px; top:630px">Contact Number</label>
    <div class="field-input" style="left:236px; top:656px; width:380px; height:54px"></div>

    <label class="field-label" style="left:236px; top:743px">Special Request</label>
    <div class="field-input" style="left:236px; top:768px; width:681px; height:154px"></div>

    <button class="confirm-button" type="button">CONFIRM</button>
  </main>

  <footer class="site-footer">
    <span class="footer-text" style="left:81px">Copyright © 2015</span>
    <span class="footer-text" style="left:249px">Lorven Executive Bed and Breakfast | Entries (RSS) and Comments (RSS)</span>
    <span class="footer-text" style="left:948px">powered by</span>
  </footer>
</body>
</html>
```